Education portal needs a new Email Creative Design

We could not decide on the creative earlier as we were unable to picture how will it look. Hence, we have added content so that we can choose the best design of all. Below is the content to be used for the email creative:
____________________________________
Did you know that 25% of all Americans have experienced at least one divorce?*
41% of first marriages end in divorce!!*

Over 1 million children are affected by divorce each year*

Become a Marriage and Family therapist - Achieve inner-happiness by helping individuals, families and couples resolve their struggles and enhance their lives.
Family Therapists are trained in various modes of therapy in order to prepare them for work with individuals, families, couples, and groups.

With proper training, you will be able to treat:
• Depression and other Affective Disorders
• Childhood Behavioral and Emotional Disorders
• Marital and Relationship Problems
• Conduct Disorder and Delinquency
• Substance Abuse
• Alcoholism
• Domestic Violence
• Severe Mental Illness
• Physical Illness

You could also qualify for financial aid* from the government to pursue this career..

Secure your life by earning upto $78,580* and attain peace of mind while helping others..

__________________________

These are the links to images we liked, but if you have something better, we would love to see them:
http://www.pexalunto.com/photo/seperated-58301947?st=7bk2913
http://www.pexalunto.com/photo/domestic-violence-72950386?st=f84m615

We are an education portal offering options of schools, colleges, universities and courses to students and working professionals.

We are looking for an email creative which has great call-to-action; be creative and research more if you wish.
Incorporate call-to-action tabs, make it colorful, include pictures and content.
Also attached are industry standard creatives for your reference, let me know if you have any questions.

Please see new files uploaded

I have uploaded a new creative made by our design team. Follow similar guidelines

For those who have not submitted their designs, please send us soon. Thanks

We thought a content brief will do more justice to this design contest hence we have updated our brief with new content to create a newer design Please submit your designs soon. Thanks

Target Market(s)

25 to 50 years working professionals

Industry/Entity Type

Government

Font styles to use
Serif
Sans Serif
Decorative
Script

Requirements
Must have
• Call-to-action

```html
<!DOCTYPE html>
<html lang="en">
<head>
<meta charset="utf-8">
<title>Marriage and Family Therapy Careers – Email Creative</title>
<link rel="stylesheet" href="https://fonts.googleapis.com/css2?family=Maven+Pro:wght@400;500;600&display=swap">
<style>
  :root {
    --page-bg: #ebebeb;
    --maroon: #5c0907;
    --frame: #6a0f0c;
    --white: #ffffff;
    --ink: #111111;
    --btn-top: #3fc6f5;
    --btn-mid: #1aa3e0;
    --btn-bottom: #0c6fae;
    --foliage: #6f7a3c;
    --foliage-light: #b7b27a;
    --brick: #9a5a48;
    --gown: #1d2650;
    --gown-deep: #141a3a;
    --icon-dark: #1b1b1b;
    --icon-scroll: #e9dcc0;
  }
  * { box-sizing: border-box; margin: 0; padding: 0; }
  html, body {
    width: 1000px; height: 1200px; overflow: hidden;
    background: var(--page-bg);
    font-family: "Maven Pro", "Trebuchet MS", sans-serif;
    color: var(--ink);
  }
  .creative {
    position: absolute; left: 12px; top: 12px;
    width: 977px; height: 1162px;
    background: var(--white);
    border: 2px solid var(--frame);
  }
  .masthead {
    position: absolute; left: 0; top: 0; width: 100%; height: 92px;
    background: var(--maroon);
    color: var(--white);
    font-size: 44px; font-weight: 400; letter-spacing: 1px;
    display: flex; align-items: center; justify-content: center;
  }
  .hero-photo {
    position: absolute; left: 0; top: 92px; width: 100%; height: 494px;
    background:
      radial-gradient(ellipse 38% 55% at 30% 80%, var(--gown) 0%, rgba(29,38,80,0) 100%),
      radial-gradient(ellipse 45% 60% at 70% 75%, var(--gown-deep) 0%, rgba(20,26,58,0) 100%),
      radial-gradient(ellipse 30% 40% at 20% 25%, rgba(183,178,122,0.8) 0%, rgba(183,178,122,0) 100%),
      linear-gradient(90deg, var(--foliage) 0%, #8a8250 40%, #a06e58 70%, var(--brick) 100%);
    border-bottom: 2px solid var(--frame);
  }
  .cta-button {
    position: absolute; left: 286px; top: 538px;
    width: 406px; height: 88px;
    border-radius: 44px;
    background: linear-gradient(180deg, var(--btn-top) 0%, var(--btn-mid) 50%, var(--btn-bottom) 100%);
    box-shadow: 0 3px 4px rgba(0,0,0,0.35);
    color: var(--white);
    font-size: 44px; font-weight: 400; letter-spacing: 0.5px;
    display: flex; align-items: center; justify-content: center; gap: 22px;
    text-decoration: none;
  }
  .cta-button svg { width: 46px; height: 40px; }
  .headline {
    position: absolute; left: 0; top: 644px; width: 100%;
    text-align: center; font-size: 31px; font-weight: 400; letter-spacing: 0.6px;
  }
  .intro {
    position: absolute; left: 44px; top: 698px; width: 890px;
    text-align: center; font-size: 15px; line-height: 20px; letter-spacing: 0.35px;
  }
  .benefits {
    position: absolute; left: 84px; top: 820px; width: 820px;
    display: grid; grid-template-columns: 414px 406px; row-gap: 20px;
    list-style: none;
  }
  .benefit { display: flex; align-items: center; gap: 30px; height: 44px; }
  .benefit-icon {
    width: 64px; height: 40px; flex: none;
    border-radius: 4px;
    background: linear-gradient(160deg, var(--icon-dark) 0%, var(--icon-dark) 55%, var(--icon-scroll) 56%, var(--icon-scroll) 100%);
  }
  .benefit-text { font-size: 18px; line-height: 23px; letter-spacing: 0.4px; }
  .divider {
    position: absolute; left: 16px; top: 1029px; width: 941px;
    border-top: 1.5px dashed var(--maroon);
  }
  .closing {
    position: absolute; left: 36px; top: 1046px; width: 904px;
    text-align: center; font-size: 15px; line-height: 20px; letter-spacing: 0.35px;
  }
  .closing-title {
    position: absolute; left: 0; top: 1097px; width: 100%;
    text-align: center; font-size: 19px; letter-spacing: 0.4px;
  }
  .footnote {
    position: absolute; left: 0; top: 1134px; width: 100%;
    text-align: center; font-size: 14px; letter-spacing: 0.3px;
  }
</style>
</head>
<body>
  <main class="creative">
    <header class="masthead">Area for Website Details</header>

    <div class="hero-photo" role="img" aria-label="Photo of smiling graduates in navy caps and gowns holding rolled diplomas outdoors"></div>

    <a class="cta-button" href="#">
      <svg viewBox="0 0 46 40" aria-hidden="true"><path d="M22 4 L6 20 L22 36 M40 4 L24 20 L40 36" fill="none" stroke="#fff" stroke-width="7" stroke-linejoin="round" stroke-linecap="round"/></svg>
      <span>Click Here</span>
      <svg viewBox="0 0 46 40" aria-hidden="true"><path d="M6 4 L22 20 L6 36 M24 4 L40 20 L24 36" fill="none" stroke="#fff" stroke-width="7" stroke-linejoin="round" stroke-linecap="round"/></svg>
    </a>

    <h1 class="headline">Become a Marriage and Family Therapist!</h1>

    <p class="intro">Did you know that 25% of all Americans have experienced at least one divorce?* 41% of first marriages end in divorce!!* Over 1 million children are affected by divorce each year.* Achieve inner-happiness by helping individuals, families and couples resolve their struggles and enhance their lives. Family Therapists are trained in various modes of therapy to prepare them for work with individuals, families, couples, and groups.</p>

    <ul class="benefits" aria-label="With proper training, you will be able to treat">
      <li class="benefit"><span class="benefit-icon" role="img" aria-label="Graduation cap with diploma icon"></span><span class="benefit-text">Depression and other<br>Affective Disorders</span></li>
      <li class="benefit"><span class="benefit-icon" role="img" aria-label="Graduation cap with diploma icon"></span><span class="benefit-text">Childhood Behavioral and<br>Emotional Disorders</span></li>
      <li class="benefit"><span class="benefit-icon" role="img" aria-label="Graduation cap with diploma icon"></span><span class="benefit-text">Marital and Relationship<br>Problems</span></li>
      <li class="benefit"><span class="benefit-icon" role="img" aria-label="Graduation cap with diploma icon"></span><span class="benefit-text">Conduct Disorder and<br>Delinquency</span></li>
      <li class="benefit"><span class="benefit-icon" role="img" aria-label="Graduation cap with diploma icon"></span><span class="benefit-text">Substance Abuse and<br>Alcoholism</span></li>
      <li class="benefit"><span class="benefit-icon" role="img" aria-label="Graduation cap with diploma icon"></span><span class="benefit-text">Domestic Violence and<br>Severe Mental Illness</span></li>
    </ul>

    <div class="divider"></div>

    <p class="closing">With proper training, you will also be able to support people living with physical illness. You could also qualify for financial aid* from the government to pursue this career.</p>
    <p class="closing-title">Secure your life by earning upto $78,580*</p>
    <p class="footnote">Attain peace of mind while helping individuals, families and couples resolve their struggles.</p>
  </main>
</body>
</html>
```